Web Design Project for an IT product called "TAVEXO"

Hello!

We need a web design for a new IT product called "TAVEXO". The product consists of 2 software applications, one is on an Android based tablet, the other on a windows 7 computer. The system is used in the production for conducting time studies (e.g. everything that has to do with time measuring in the production). The design should include the company logo ("DRUL"), and the logo of the methodology used ("VOMI" - see www.vomi-example.de), the rest is up to you! We already made a concept for the app logo, but it can be tweaked in any way...
Updates

Will upload a document with exact description!

Updated the files... Made some screenshots of the app on the Android device & Windows 7

Reason: Will make a poll & let you know the decision tomorrow!

Target Market(s)

Larger production companies middle management, technology departments

Industry/Entity Type

Computer

Requirements
Must have
• - company logo "DRUL" - included
- methodology logo "VOMI" (see www.vomi-example.de) - included
Nice to have
• - our logo of the app tweaked and somehow integrated

```html
<!DOCTYPE html>
<html lang="en">
<head>
<meta charset="utf-8">
<title>TAVEXO 3.0 – Time Study System</title>
<link href="https://fonts.googleapis.com/css2?family=Quicksand:wght@400;500&family=Arimo:wght@400;700&display=swap" rel="stylesheet">
<style>
  :root {
    --page-bg: #ffffff;
    --text: #555555;
    --heading: #333333;
    --link: #2a8ac4;
    --note-bg: #f5ebb6;
    --note-label-bg: #e9d46c;
    --note-label-text: #7a6824;
    --note-text: #b8893a;
    --band-bg: #1d262b;
    --band-text: #e9ecee;
    --footer-bg: #2f3c45;
    --footer-heading: #8fc9e8;
    --footer-text: #a9b6be;
    --footer-link: #e6ebee;
    --copyright: #98a4ab;
    --art-dark: #1b1f24;
    --art-light: #f2f2f2;
  }
  * { margin: 0; padding: 0; box-sizing: border-box; }
  html, body { width: 1200px; height: 900px; overflow: hidden; }
  body {
    position: relative;
    background: var(--page-bg);
    font-family: "Arimo", Arial, sans-serif;
    color: var(--text);
    font-size: 12px;
  }
  a { text-decoration: none; }

  .intro-tail { position: absolute; left: 201px; top: -7px; font-size: 12px; }

  .note {
    position: absolute; left: 201px; top: 20px; width: 494px; height: 92px;
    background: var(--note-bg);
  }
  .note-label {
    position: absolute; left: 0; top: 0; width: 62px; height: 23px;
    background: var(--note-label-bg); color: var(--note-label-text);
    font-size: 11px; font-weight: 700; line-height: 23px; padding-left: 14px;
  }
  .note-text {
    position: absolute; left: 34px; top: 33px; width: 440px;
    color: var(--note-text); line-height: 20px;
  }
  .note-text a { color: #5a4a20; }

  .divider {
    position: absolute; left: 201px; top: 140px; width: 494px;
    border-top: 2px dotted #dedede;
  }

  .advantages-title {
    position: absolute; left: 201px; top: 177px;
    font-size: 17px; font-weight: 700; color: var(--heading);
  }
  .advantages-list {
    position: absolute; top: 205px; list-style: none; line-height: 20px; width: 236px;
  }
  .advantages-list.col-a { left: 201px; }
  .advantages-list.col-b { left: 459px; }
  .advantages-list li::before { content: "➔"; font-size: 10px; color: #444; margin: 0 4px 0 3px; }
  .read-more { position: absolute; left: 201px; top: 316px; color: var(--link); }

  .product-art {
    position: absolute; left: 752px; top: 0; width: 322px; height: 325px;
    background: linear-gradient(160deg, var(--art-dark) 0%, #2c333a 35%, var(--art-light) 40%, #ffffff 100%);
  }

  .pricing-band {
    position: absolute; left: 0; top: 379px; width: 1200px; height: 193px;
    background: var(--band-bg); text-align: center;
  }
  .pricing-band h2 {
    margin-top: 47px; font-family: "Quicksand", sans-serif; font-weight: 400;
    font-size: 25px; line-height: 28px; letter-spacing: 1px; color: var(--band-text);
  }
  .pricing-button {
    display: inline-block; margin-top: 9px; width: 219px; height: 40px;
    background: linear-gradient(#ffffff, #e6e6e6); color: #333;
    font-family: "Quicksand", sans-serif; font-weight: 500; font-size: 15px;
    line-height: 40px; letter-spacing: 0.5px;
  }

  .site-footer {
    position: absolute; left: 0; top: 572px; width: 1200px; height: 328px;
    background: var(--footer-bg);
  }
  .footer-col { position: absolute; top: 50px; width: 195px; }
  .footer-col h3 {
    font-size: 13px; font-weight: 700; letter-spacing: 1px; text-transform: uppercase;
    color: var(--footer-heading); margin-bottom: 11px;
  }
  .footer-col p { color: var(--footer-text); line-height: 20px; margin-bottom: 8px; }
  .footer-col strong { color: var(--footer-text); }
  .footer-col ul { list-style: none; }
  .footer-col li { line-height: 24.6px; margin-top: -3px; }
  .footer-col li a { color: var(--footer-link); }
  .col-training { left: 163px; }
  .col-contacts { left: 391px; }
  .col-features { left: 619px; }
  .col-nav { left: 847px; }
  .copyright {
    position: absolute; top: 273px; width: 100%; text-align: center;
    font-size: 11px; font-weight: 700; color: var(--copyright);
  }
</style>
</head>
<body>
  <p class="intro-tail">production.</p>

  <aside class="note">
    <span class="note-label">NOTE</span>
    <p class="note-text">The system was very successful on the slovenian market; nowadays more than 50 companies are using it plus both machine faculties. <a href="#">Learn more »</a></p>
  </aside>

  <div class="divider"></div>

  <h2 class="advantages-title">Advantages of the system TAVEXO 3.0:</h2>
  <ul class="advantages-list col-a">
    <li>An extremely competitive price</li>
    <li>Fast and easy time data gathering</li>
    <li>Multitask use in the field of time and work study</li>
    <li>Possibility of upgradin the system</li>
  </ul>
  <ul class="advantages-list col-b">
    <li>The evaluation of the recording is done automatically</li>
    <li>Automatical statistical analysis</li>
    <li>WiFi support for data transfer</li>
    <li>Photo / video documentation possibilites</li>
  </ul>
  <a class="read-more" href="#">Read all advantages »</a>

  <div class="product-art" role="img" aria-label="Tablet showing the TAVEXO app with a white app logo card in front"></div>

  <section class="pricing-band">
    <h2>The price of the system Tavexo 3.0 without tablet devices are<br>quantity-dependant (number of users/methods):</h2>
    <a class="pricing-button" href="#">Tavexo 3.0 Pricing »</a>
  </section>

  <footer class="site-footer">
    <div class="footer-col col-training">
      <h3>Training for Tavexo 3.0</h3>
      <p>Training is completely practical; the analyst(s) conduct a time study in the client production and evaluate data on the PC. A normal training usually takes about 4-6 hours.</p>
      <p>The price depends on the travelling distance.</p>
    </div>
    <div class="footer-col col-contacts">
      <h3>Contacts</h3>
      <p><strong>DRUL, Inc.</strong><br>123 Name Ave, Suite 456<br>City Name, ST 12345</p>
      <p>P: (123) 456-7890<br>E: example@email.com</p>
    </div>
    <div class="footer-col col-features">
      <h3>Tavexo 3.0 Features</h3>
      <ul>
        <li><a href="#">Feature name one</a></li>
        <li><a href="#">Feature name two</a></li>
        <li><a href="#">Feature name three</a></li>
        <li><a href="#">Feature name four</a></li>
        <li><a href="#">Feature name five</a></li>
        <li><a href="#">Feature name six</a></li>
      </ul>
    </div>
    <div class="footer-col col-nav">
      <h3>Main Navigation</h3>
      <ul>
        <li><a href="#">Home</a></li>
        <li><a href="#">About</a></li>
        <li><a href="#">Services</a></li>
        <li><a href="#">Price</a></li>
        <li><a href="#">F.A.Q</a></li>
        <li><a href="#">Contacts</a></li>
      </ul>
    </div>
    <p class="copyright">© 2012 DRUL. All Rights Reserved.</p>
  </footer>
</body>
</html>
```